Brindexa Business Card

Our mission is to craft high value solutions combining consulting and edge technologies for helping big and middle sized companies in the Digital Transformation Process that they must face. We think that this transformation will impact business processes and people skills in a new manner. Brindexa's value proposition is to collaborate with our clients for creating new competitive advantages based on technology, processes and people.
We already have a logo designed through your platform.

Industry/Entity Type

Business

```html
<!DOCTYPE html>
<html lang="en">
<head>
<meta charset="UTF-8">
<title>Brindexa Business Card</title>
<link href="https://fonts.googleapis.com/css2?family=Open+Sans:wght@400;600;700&display=swap" rel="stylesheet">
<style>
  :root {
    --bg: #c9c9c9;
    --card-white: #ffffff;
    --card-dark: #3c3c3c;
    --band-dark: #3a3a3a;
    --accent-blue: #1d9ad6;
    --accent-red: #e4202a;
    --text-dark: #3d3d3d;
    --text-mid: #4a4a4a;
  }
  * { margin: 0; padding: 0; box-sizing: border-box; }
  html, body { width: 1200px; height: 894px; overflow: hidden; }
  body {
    background: var(--bg);
    font-family: "Open Sans", Arial, sans-serif;
    position: relative;
  }
  .card {
    position: absolute;
    top: 292px;
    width: 540px;
    height: 310px;
    overflow: hidden;
    clip-path: polygon(14px 0, calc(100% - 14px) 0, 100% 14px, 100% calc(100% - 14px), calc(100% - 14px) 100%, 14px 100%, 0 calc(100% - 14px), 0 14px);
  }
  .card-front { left: 40px; background: var(--card-white); }
  .card-back { left: 620px; background: var(--card-dark); }

  .band { position: absolute; height: 12px; }
  .band-top-dark { top: 0; left: 0; width: 56%; background: var(--band-dark); }
  .band-top-blue { top: 0; right: 0; width: 44%; background: var(--accent-blue); height: 9px; }
  .band-bottom-blue { bottom: 0; left: 0; width: 36%; background: var(--accent-blue); height: 9px; }
  .band-bottom-dark { bottom: 0; right: 0; width: 64%; background: var(--band-dark); }

  .contact {
    position: absolute;
    top: 42px;
    right: 290px;
    text-align: right;
    color: var(--text-mid);
  }
  .person-name { color: var(--accent-red); font-weight: 700; font-size: 19px; letter-spacing: .3px; }
  .person-role { font-size: 15px; color: var(--text-dark); letter-spacing: .5px; margin-bottom: 16px; }
  .address { font-size: 12.5px; line-height: 18px; margin-bottom: 10px; }
  .contact-line {
    font-size: 12.5px; line-height: 19px;
    display: flex; justify-content: flex-end; align-items: center; gap: 6px;
  }
  .contact-line svg { width: 14px; height: 14px; flex: none; }

  .brand {
    position: absolute;
    display: flex; align-items: center; gap: 12px;
  }
  .brand-dot { width: 30px; height: 30px; border-radius: 50%; background: var(--accent-blue); }
  .brand-name { font-weight: 600; font-size: 34px; letter-spacing: 1px; }
  .brand-front { left: 290px; top: 130px; }
  .brand-front .brand-name { color: var(--text-dark); }

  .back-strip { position: absolute; background: var(--accent-blue); width: 10px; }
  .back-strip-left { left: 0; top: 22px; height: 90px; }
  .back-strip-right { right: 0; bottom: 22px; height: 90px; }
  .brand-back { left: 50%; top: 108px; transform: translateX(-50%); }
  .brand-back .brand-name { color: #ffffff; }
  .back-web {
    position: absolute; top: 190px; width: 100%; text-align: center;
    color: #e8e8e8; font-size: 15px; letter-spacing: 1.5px;
  }
</style>
</head>
<body>

<section class="card card-front" aria-label="Business card front">
  <div class="band band-top-dark"></div>
  <div class="band band-top-blue"></div>
  <div class="band band-bottom-blue"></div>
  <div class="band band-bottom-dark"></div>

  <div class="contact">
    <p class="person-name">MARTIN CALLOWAY</p>
    <p class="person-role">GENERAL MANAGER</p>
    <p class="address">Calloway St, 218B<br>Lorem City, Northvale</p>
    <p class="contact-line">001 482 915 307
      <svg viewBox="0 0 14 14" aria-hidden="true"><circle cx="7" cy="7" r="7" fill="var(--accent-red)"/><path d="M4.5 3.5 6 5 5.2 6c.5 1.2 1.6 2.3 2.8 2.8L9 8l1.5 1.5-1 1C6.5 10.3 3.7 7.5 3.5 4.5z" fill="#fff"/></svg></p>
    <p class="contact-line">001 482 915 307
      <svg viewBox="0 0 14 14" aria-hidden="true"><circle cx="7" cy="7" r="7" fill="var(--accent-red)"/><rect x="4" y="4" width="6" height="6" rx="1" fill="none" stroke="#fff" stroke-width="1.2"/></svg></p>
    <p class="contact-line">info@brindexa-hub.com
      <svg viewBox="0 0 14 14" aria-hidden="true"><circle cx="7" cy="7" r="7" fill="var(--accent-red)"/><rect x="3.5" y="4.5" width="7" height="5" fill="#fff"/><path d="M3.5 4.5 7 7.5l3.5-3" fill="none" stroke="var(--accent-red)" stroke-width=".8"/></svg></p>
    <p class="contact-line">www.brindexa-hub.com
      <svg viewBox="0 0 14 14" aria-hidden="true"><circle cx="7" cy="7" r="7" fill="var(--accent-red)"/><circle cx="7" cy="7" r="3.6" fill="none" stroke="#fff" stroke-width="1"/><path d="M3.4 7h7.2M7 3.4v7.2" stroke="#fff" stroke-width=".8"/></svg></p>
  </div>

  <div class="brand brand-front">
    <span class="brand-dot"></span>
    <span class="brand-name">BRINDEXA</span>
  </div>
</section>

<section class="card card-back" aria-label="Business card back">
  <div class="back-strip back-strip-left"></div>
  <div class="back-strip back-strip-right"></div>
  <div class="brand brand-back">
    <span class="brand-dot"></span>
    <span class="brand-name">BRINDEXA</span>
  </div>
  <p class="back-web">www.brindexa-hub.com</p>
</section>

</body>
</html>
```